Web Design Project

Update to the following web page.

www.velorintadvisory.com

We would like a full screen website, similar to the ones found here. http://www.pixelquorra.com/websites/fullscreen/

We also really like this site
http://brightmoleworks.com/

We would like new images and graphics.

Menu should be
1. Audit Defense
2. Education
3. Consulting
4. Outsourcing
5. Our Team
6. Store
7. Contact Us

Incorporate our new logo and colors. File is attached. The blue logo.

We want to add this tag line: "A passion for compliance through homecare and hospice training, education, and consulting."

Target Market(s)

Home Health Care Companies

Industry/Entity Type

Defense

Requirements
Must have
• Display our contact information in header and footer.

```html
<!DOCTYPE html>
<html lang="en">
<head>
<meta charset="utf-8">
<title>Velorint Advisory</title>
<link rel="stylesheet" href="https://fonts.googleapis.com/css2?family=Fira+Sans+Condensed:wght@300;400;500;700&display=swap">
<style>
:root{
  --ink:#1f1f1f;
  --topbar:#000000;
  --white:#ffffff;
  --brand:#35578f;
  --brand-soft:#8ea2c4;
  --highlight-top:#5677a8;
  --highlight-bottom:#2f5189;
  --card-text:#3a3a3a;
  --divider:#d4d4d4;
  --footer:#0b0b0b;
  --footer-rule:#8a8a8a;
  --footer-text:#a9a9a9;
  --hero-sky:#3a5566;
  --hero-dark:#141a20;
  --tab:#1b1b1b;
}
*{box-sizing:border-box;margin:0;padding:0}
html,body{width:1200px;height:726px;overflow:hidden;background:var(--white)}
body{font-family:"Fira Sans Condensed",sans-serif;color:var(--ink)}
.page{position:relative;width:1200px;height:726px;overflow:hidden}

.topbar{position:absolute;left:0;top:0;width:1200px;height:21px;background:var(--topbar);color:#e8e8e8;font-size:10.5px}
.topbar-contact{position:absolute;right:185px;top:4px;display:flex;align-items:center;gap:7px}

.header{position:absolute;left:0;top:21px;width:1200px;height:90px;background:var(--white)}
.brand{position:absolute;left:220px;top:0;height:90px;display:flex;align-items:center}
.brand-mark{width:26px;height:26px;background:var(--brand);margin-right:14px}
.brand-name{font-size:25px;font-weight:400;color:var(--brand-soft);letter-spacing:.5px}
.brand-rule{position:absolute;left:100px;top:0;width:2px;height:90px;background:#3a3a3a}
.nav{position:absolute;right:185px;top:37px;display:flex;gap:10.5px;list-style:none}
.nav a{font-size:13px;font-weight:500;color:var(--ink);text-decoration:none}

.hero{position:absolute;left:0;top:111px;width:1200px;height:321px;
  background:linear-gradient(180deg,#4a5d68 0%,var(--hero-sky) 35%,#2a3238 65%,var(--hero-dark) 100%)}
.hero-copy{position:absolute;left:0;top:114px;width:1200px;text-align:center;color:var(--white)}
.hero-title{font-size:32px;font-weight:700;line-height:40px;letter-spacing:-.2px}
.hero-link{display:inline-block;margin-top:9px;font-size:17px;font-weight:700;color:var(--white);text-decoration:none}
.slide-tab{position:absolute;top:121px;width:34px;height:84px;background:var(--tab);color:#9a9a9a;font-size:20px;display:flex;align-items:center;justify-content:center;opacity:.85}
.slide-tab.prev{left:0;border-radius:0 4px 4px 0}
.slide-tab.next{right:0;border-radius:4px 0 0 4px}

.services{position:absolute;left:336px;top:421px;width:568px;height:199px;display:flex;background:var(--white);box-shadow:0 0 4px rgba(0,0,0,.08)}
.service{width:142px;height:199px;text-align:center;padding-top:22px;border-left:1px dashed var(--divider)}
.service:first-child{border-left:none}
.service.is-active{background:linear-gradient(180deg,var(--highlight-top),var(--highlight-bottom));border-left:none;color:var(--white)}
.service.is-active + .service{border-left:none}
.service-icon{width:40px;height:36px;display:block;margin:0 auto}
.service-title{font-size:13px;font-weight:400;margin-top:15px}
.service-text{font-size:10.5px;font-weight:300;line-height:14px;color:var(--card-text);width:100px;margin:10px auto 0}
.service.is-active .service-text{color:#f0f3f8}

.footer{position:absolute;left:0;top:620px;width:1200px;height:106px;background:var(--footer);border-top:3px solid var(--footer-rule);text-align:center;color:var(--footer-text);font-size:11.5px;line-height:18px}
.footer-info{padding-top:24px}
.social{display:flex;justify-content:center;gap:6px;margin-top:7px}
.social span{width:13px;height:13px;border-radius:50%;background:#8d8d8d;display:block}
</style>
</head>
<body>
<div class="page">
  <div class="topbar">
    <div class="topbar-contact">
      <svg width="12" height="8" viewBox="0 0 12 8" aria-hidden="true"><rect width="12" height="8" fill="#6d83a8"/><path d="M0 0 L6 4.5 L12 0" fill="none" stroke="#1a1a1a" stroke-width="1"/></svg>
      <span>18, Harlow Lane, Brisbane, CA 31720, Ph : 407153</span>
    </div>
  </div>

  <header class="header">
    <div class="brand">
      <span class="brand-mark"></span>
      <span class="brand-rule"></span>
      <span class="brand-name" style="margin-left:50px">Velorint Advisory</span>
    </div>
    <ul class="nav">
      <li><a href="#">Audit Defense</a></li>
      <li><a href="#">Education</a></li>
      <li><a href="#">Consulting</a></li>
      <li><a href="#">Outsourcing</a></li>
      <li><a href="#">Our Team</a></li>
      <li><a href="#">Store</a></li>
      <li><a href="#">Contact Us</a></li>
    </ul>
  </header>

  <section class="hero" role="img" aria-label="Photograph of a city skyline at dusk with lit office towers under a cloudy blue sky">
    <div class="slide-tab prev">&#10094;</div>
    <div class="hero-copy">
      <h1 class="hero-title">A passion for compliance through homecare<br>and hospice training, education, and consulting.</h1>
      <a class="hero-link" href="#">LEARN MORE &raquo;</a>
    </div>
    <div class="slide-tab next">&#10095;</div>
  </section>

  <section class="services">
    <article class="service">
      <svg class="service-icon" viewBox="0 0 40 36" aria-hidden="true"><path d="M20 3 L37 18 L33 18 L33 34 L24 34 L24 24 L16 24 L16 34 L7 34 L7 18 L3 18 Z" fill="var(--brand)"/><path d="M9 17 L20 7 L31 17" fill="none" stroke="#fff" stroke-width="2"/></svg>
      <h2 class="service-title">Homecare</h2>
      <p class="service-text">Lorem ipsum dolor sit amet, consectetur adipisicing elit, sed do eiusmod tempor incididunt ut labore et dolore magna aliqua.</p>
    </article>
    <article class="service is-active">
      <svg class="service-icon" viewBox="0 0 40 36" aria-hidden="true"><rect x="17" y="10" width="14" height="24" rx="7" fill="none" stroke="#fff" stroke-width="2.5"/><line x1="24" y1="10" x2="24" y2="18" stroke="#fff" stroke-width="2"/><path d="M17 22 C10 20 10 10 13 6 C15 3 19 4 20 8" fill="none" stroke="#fff" stroke-width="2.5"/></svg>
      <h2 class="service-title">Hospice training</h2>
      <p class="service-text">Lorem ipsum dolor sit amet, consectetur adipisicing elit, sed do eiusmod tempor incididunt ut labore et dolore magna aliqua.</p>
    </article>
    <article class="service">
      <svg class="service-icon" viewBox="0 0 40 36" aria-hidden="true"><path d="M10 30 C6 18 14 6 34 3 C35 20 26 31 13 29 Z" fill="var(--brand)"/><path d="M7 34 L24 14" stroke="#fff" stroke-width="2"/></svg>
      <h2 class="service-title">Education</h2>
      <p class="service-text">Lorem ipsum dolor sit amet, consectetur adipisicing elit, sed do eiusmod tempor incididunt ut labore et dolore magna aliqua.</p>
    </article>
    <article class="service">
      <svg class="service-icon" viewBox="0 0 40 36" aria-hidden="true"><path d="M3 19 C3 9 11 3 20 3 C29 3 37 9 37 19 Z" fill="var(--brand)"/><path d="M20 19 L20 30 C20 34 15 34 15 30" fill="none" stroke="var(--brand)" stroke-width="2.5"/></svg>
      <h2 class="service-title">Consulting</h2>
      <p class="service-text">Lorem ipsum dolor sit amet, consectetur adipisicing elit, sed do eiusmod tempor incididunt ut labore et dolore magna aliqua.</p>
    </article>
  </section>

  <footer class="footer">
    <p class="footer-info">18, Harlow Lane, Brisbane, CA 31720, Ph : 407153<br>Copyright@2013,Velorint Advisory, Terms &amp; Privacy Policy</p>
    <div class="social">
      <span role="img" aria-label="Social network link"></span>
      <span role="img" aria-label="Social network link"></span>
      <span role="img" aria-label="Video channel link"></span>
    </div>
  </footer>
</div>
</body>
</html>
```